Anchored Willow Website

Would like a website designed for my fitness and nutrition coaching company Anchor Willow. I have a company logo and would like to keep the page layout clean and simple. Needs to look great on computer and mobile devices.

Target Market(s)

Target market is individuals looking to make changes in their health and nutrition with the help of an online coach.

Industry/Entity Type

Fitness

Number of Pages Required

2 page

Colors
3176b5
0355a3
85acd3
cedeed
f8fcfd
ffffff

Requirements
Must have
• The first page should have the company logo and name towards the top and below that client before and after photos scrolling or displaying in some manner. Also would like a section that states services offered and a section about myself since I am the primary coach for clients.

```html
<!DOCTYPE html>
<html lang="en">
<head>
<meta charset="utf-8">
<title>Anchored Willow – Personal Fitness Coach</title>
<link href="https://fonts.googleapis.com/css2?family=Montserrat:wght@400;600;700;800&family=Open+Sans:ital,wght@0,400;0,600;1,400&display=swap" rel="stylesheet">
<style>
:root{
  --blue:#1e73be;
  --blue-deep:#0355a3;
  --blue-mid:#3176b5;
  --blue-soft:#85acd3;
  --blue-pale:#cedeed;
  --ice:#f8fcfd;
  --white:#ffffff;
  --ink:#222831;
  --text:#6b6f76;
  --line:#e3e6ea;
  --dark:#16191d;
}
*{box-sizing:border-box;margin:0;padding:0}
html,body{width:1200px;height:4489px;overflow:hidden}
body{font-family:"Open Sans",Arial,sans-serif;color:var(--text);background:var(--white);position:relative}
section,header,footer{position:relative;width:1200px;overflow:hidden}

/* header */
.site-header{height:120px;background:var(--white)}
.topbar{position:absolute;right:0;top:0;width:495px;height:36px;background:var(--blue);display:flex;align-items:center;padding-left:30px;gap:10px;color:var(--white);font-size:12px;white-space:nowrap}
.topbar .mail{margin-right:60px}
.topbar .dot{width:20px;height:20px;border-radius:50%;background:var(--white)}
.brand{position:absolute;left:150px;top:20px;display:flex;flex-direction:column;align-items:center;gap:8px}
.brand .mark{width:44px;height:44px;background:var(--blue)}
.brand .name{font-family:"Montserrat",sans-serif;font-weight:700;font-size:17px;color:var(--blue);letter-spacing:.5px;text-transform:uppercase;white-space:nowrap}
.nav{position:absolute;right:150px;top:62px;display:flex;align-items:center;gap:30px;font-family:"Montserrat",sans-serif;font-size:13px;font-weight:600;color:var(--ink);text-transform:uppercase}
.nav .active{color:var(--blue);border-bottom:3px solid var(--blue);padding-bottom:6px;margin-top:9px}
.nav .signin{border:1px solid var(--line);padding:10px 16px}

/* hero */
.hero{height:524px;background:radial-gradient(ellipse at 30% 40%,#7f8f9f 0%,#3d4e62 35%,#1d2f4a 70%,#142440 100%)}
.hero h1{position:absolute;left:155px;top:170px;font-family:"Montserrat",sans-serif;font-weight:800;font-size:28px;color:var(--white);text-transform:uppercase;white-space:nowrap}
.hero .sub{position:absolute;left:155px;top:210px;font-family:"Montserrat",sans-serif;font-size:24px;color:var(--white);text-transform:uppercase;letter-spacing:1px;white-space:nowrap}
.btn{display:inline-flex;align-items:center;justify-content:center;font-family:"Montserrat",sans-serif;font-weight:700;font-size:13px;text-transform:uppercase;color:var(--white);letter-spacing:.5px;white-space:nowrap}
.btn-solid{background:var(--blue)}
.btn-line{border:2px solid rgba(255,255,255,.8)}
.hero .demo{position:absolute;left:155px;top:275px;width:145px;height:46px}
.hero .join{position:absolute;left:325px;top:275px;width:155px;height:46px}
.polaroid{position:absolute;background:var(--white);padding:10px 10px 0;box-shadow:0 10px 30px rgba(0,0,0,.4)}
.polaroid .photo{width:100%;height:310px}
.polaroid .label{height:46px;display:flex;align-items:center;justify-content:center;font-family:"Montserrat",sans-serif;font-weight:700;font-size:24px;color:var(--ink)}
.polaroid.before{left:696px;top:54px;width:180px;transform:rotate(-3deg)}
.polaroid.before .photo{background:linear-gradient(160deg,#c86f4f,#24a6d8 60%,#1d7fb5)}
.polaroid.after{left:870px;top:58px;width:180px;transform:rotate(3deg)}
.polaroid.after .photo{background:linear-gradient(170deg,#ded6cc,#2eafc6 55%,#6a6d75)}
.dots{position:absolute;left:848px;top:456px;display:flex;gap:8px}
.dots span{width:13px;height:13px;border-radius:50%;border:2px solid var(--blue-soft)}
.dots span.on{background:var(--blue-soft)}

/* section titles */
.section-mark{width:40px;height:40px;background:var(--blue);margin:0 auto}
.section-title{font-family:"Montserrat",sans-serif;font-weight:800;font-size:32px;text-align:center;color:var(--blue);text-transform:uppercase}
.section-title span{color:#555}
.intro{width:740px;margin:0 auto;text-align:center;font-size:13.5px;line-height:22px}

/* services */
.services{height:1068px;padding-top:70px}
.services .section-title{margin-top:18px}
.services .intro{margin-top:28px}
.service-grid{position:absolute;left:156px;top:394px;display:grid;grid-template-columns:repeat(3,246px);column-gap:66px;row-gap:96px}
.service-card{height:188px;border:1px solid var(--line);position:relative;text-align:center;padding:76px 24px 0}
.service-icon{position:absolute;left:50%;top:-38px;width:76px;height:76px;margin-left:-38px;transform:rotate(45deg);background:var(--blue);border:4px solid var(--white);outline:2px solid var(--blue)}
.service-icon svg{transform:rotate(-45deg);width:100%;height:100%}
.service-card h3{font-family:"Montserrat",sans-serif;font-weight:700;font-size:17px;color:var(--ink);line-height:21px;min-height:42px;display:flex;align-items:center;justify-content:center}
.service-card p{font-size:12px;line-height:17px;margin-top:8px}
.services .details{position:absolute;left:516px;top:942px;width:182px;height:46px}

/* video */
.video{height:512px;background:radial-gradient(ellipse at 55% 45%,#3b4553 0%,#1a1f26 45%,#0e1114 100%)}
.video .figure{position:absolute;left:330px;top:70px;width:540px;height:380px;border-radius:50%;background:radial-gradient(ellipse at 50% 60%,#2c4a78 0%,#1b2940 50%,transparent 72%)}
.play{position:absolute;left:525px;top:150px;width:150px;height:150px;transform:rotate(45deg);border:2px solid var(--blue-soft);background:rgba(3,85,163,.25)}
.play-label{position:absolute;left:0;top:243px;width:1200px;display:flex;justify-content:center;align-items:center;gap:10px;font-family:"Montserrat",sans-serif;font-weight:600;font-size:14px;color:var(--white);text-transform:uppercase}
.play-label i{width:26px;height:26px;border-radius:50%;border:1px solid var(--white);display:flex;align-items:center;justify-content:center}

/* coach */
.coach{height:853px;background:var(--white)}
.coach .portrait{position:absolute;left:90px;top:80px;width:480px;height:773px;background:linear-gradient(180deg,#f1f3f5 0%,#d8dde3 30%,#2a6fc0 55%,#1a5aa8 100%);border-radius:200px 200px 0 0}
.coach .info{position:absolute;left:628px;top:170px;width:430px}
.coach h2{font-family:"Montserrat",sans-serif;font-weight:800;font-size:22px;color:var(--ink);text-transform:uppercase}
.coach .role{font-family:"Montserrat",sans-serif;font-weight:600;font-size:12px;color:var(--blue);text-transform:uppercase;margin-top:2px}
.coach p{font-size:13px;line-height:21px;margin-top:14px}
.coach h4{font-family:"Montserrat",sans-serif;font-weight:700;font-size:13px;color:var(--blue);text-transform:uppercase;margin-top:36px}
.social{display:flex;gap:8px;margin-top:16px}
.social span{width:26px;height:26px;border-radius:50%}
.coach .about{margin-top:66px;width:200px;height:48px}

/* register */
.register{height:299px;background:linear-gradient(100deg,#1a2433 0%,#2b3746 45%,#46535e 70%,#1b2532 100%);text-align:center;color:var(--white)}
.register h2{font-family:"Montserrat",sans-serif;font-weight:800;font-size:28px;text-transform:uppercase;margin-top:70px}
.register p{font-size:13px;margin-top:12px}
.register .signup{margin-top:44px;width:196px;height:46px}

/* feedback */
.feedback{height:724px;padding-top:72px}
.feedback .section-title{margin-top:18px}
.feedback .intro{margin-top:30px}
.quotes{position:absolute;left:156px;top:299px;display:grid;grid-template-columns:repeat(3,281px);column-gap:25px}
.quote{height:192px;background:var(--blue);color:var(--white);font-style:italic;font-size:13px;line-height:22px;padding:22px 20px}
.person{display:flex;align-items:center;gap:16px;margin-top:22px;padding-left:20px}
.avatar{width:68px;height:68px;transform:rotate(45deg);background:linear-gradient(135deg,#cfd6dd,#8f9aa5);border:3px solid var(--white);outline:1px solid var(--line)}
.person b{display:block;font-family:"Montserrat",sans-serif;font-size:12.5px;color:var(--ink);text-transform:uppercase;font-weight:600}
.person small{font-size:11.5px}

/* footer */
.site-footer{height:270px;background:linear-gradient(180deg,#16191d,#0d0f12);text-align:center}
.site-footer .brand{position:static;margin:48px auto 0;width:max-content}
.footer-nav{display:flex;justify-content:center;gap:24px;margin-top:40px;font-family:"Montserrat",sans-serif;font-size:12px;color:#c8ccd2;text-transform:uppercase}
.footer-nav .active{color:var(--blue-soft)}
.footer-nav span+span::before{content:"|";margin-right:24px;color:#555}
.footer-social{display:flex;justify-content:center;gap:12px;margin-top:38px}
.footer-social span{width:26px;height:26px;border-radius:50%;background:var(--blue-deep)}
.copyright{height:119px;text-align:center;font-size:12px;color:#777;padding-top:55px;position:relative}
.copyright .up{position:absolute;left:582px;bottom:0;width:36px;height:18px;background:var(--blue);clip-path:polygon(50% 0,100% 100%,0 100%)}
</style>
</head>
<body>

<header class="site-header">
  <div class="topbar">
    <span class="mail">✉ hello@anchoredwillow.com</span>
    <span class="dot"></span><span class="dot"></span><span class="dot"></span>
  </div>
  <div class="brand"><span class="mark"></span><span class="name">Anchored Willow</span></div>
  <nav class="nav">
    <span class="active">Home</span><span>Services</span><span>Success Story</span><span>About</span><span>Contacts</span><span class="signin">Sign In</span>
  </nav>
</header>

<section class="hero">
  <h1>Your Personal Fitness Coach</h1>
  <div class="sub">Can Make You Fit Forever</div>
  <a class="btn btn-solid demo">Demo Video &nbsp;»</a>
  <a class="btn btn-line join">Join Now &nbsp;»</a>
  <div class="polaroid before"><div class="photo" role="img" aria-label="Client photo before coaching"></div><div class="label">Before</div></div>
  <div class="polaroid after"><div class="photo" role="img" aria-label="Client photo after coaching"></div><div class="label">After</div></div>
  <div class="dots"><span></span><span class="on"></span><span></span></div>
</section>

<section class="services">
  <div class="section-mark"></div>
  <h2 class="section-title">Services <span>We Offered</span></h2>
  <p class="intro">Lorem ipsum dolor sit amet, consectetur adipisicing elit, sed do eiusmod tempor incididunt ut labore et dolore magna aliqua. Ut enim ad minim veniam, quis nostrud exercitation ullamco laboris nisi ut aliquip ex ea commodo consequat.</p>
  <div class="service-grid">
    <div class="service-card"><div class="service-icon"><svg viewBox="0 0 76 76"><circle cx="38" cy="38" r="14" fill="none" stroke="#fff" stroke-width="2.5"/><path d="M32 38h12M38 32v12" stroke="#fff" stroke-width="2.5"/></svg></div><h3>Personalized<br>Nutrition Plan</h3><p>Lorem ipsum dolor sit amet, consectetur tempor incididunt ut labore.</p></div>
    <div class="service-card"><div class="service-icon"><svg viewBox="0 0 76 76"><circle cx="38" cy="30" r="5" fill="#fff"/><path d="M28 50l10-14 10 14" fill="none" stroke="#fff" stroke-width="2.5"/></svg></div><h3>Professional Trainer</h3><p>Lorem ipsum dolor sit amet, consectetur tempor incididunt ut labore.</p></div>
    <div class="service-card"><div class="service-icon"><svg viewBox="0 0 76 76"><path d="M24 38h28M24 32v12M52 32v12M20 35v6M56 35v6" stroke="#fff" stroke-width="3"/></svg></div><h3>Individual Fitness<br>Program</h3><p>Lorem ipsum dolor sit amet, consectetur tempor incididunt ut labore.</p></div>
    <div class="service-card"><div class="service-icon"><svg viewBox="0 0 76 76"><rect x="24" y="28" width="28" height="20" rx="2" fill="none" stroke="#fff" stroke-width="2.5"/><path d="M24 34h28" stroke="#fff" stroke-width="3"/></svg></div><h3>Easy Online Payment<br>Method</h3><p>Lorem ipsum dolor sit amet, consectetur tempor incididunt ut labore.</p></div>
    <div class="service-card"><div class="service-icon"><svg viewBox="0 0 76 76"><rect x="25" y="26" width="26" height="24" fill="none" stroke="#fff" stroke-width="2.5"/><path d="M25 33h26M31 22v6M45 22v6" stroke="#fff" stroke-width="2.5"/></svg></div><h3>Flexible Schedule</h3><p>Lorem ipsum dolor sit amet, consectetur tempor incididunt ut labore.</p></div>
    <div class="service-card"><div class="service-icon"><svg viewBox="0 0 76 76"><rect x="23" y="28" width="30" height="20" fill="none" stroke="#fff" stroke-width="2.5"/><circle cx="32" cy="38" r="4" fill="#fff"/><path d="M40 35h9M40 41h9" stroke="#fff" stroke-width="2"/></svg></div><h3>Lifetime Membership<br>Facility</h3><p>Lorem ipsum dolor sit amet, consectetur tempor incididunt ut labore.</p></div>
  </div>
  <a class="btn btn-solid details">Read Details &nbsp;»</a>
</section>

<section class="video">
  <div class="figure" role="img" aria-label="Athlete stretching backwards over an exercise ball"></div>
  <div class="play"></div>
  <div class="play-label">Play Video <i>›</i></div>
</section>

<section class="coach">
  <div class="portrait" role="img" aria-label="Portrait of the personal fitness coach in a blue shirt, arms crossed"></div>
  <div class="info">
    <h2>Evan Marsh</h2>
    <div class="role">Personal Fitness Coach</div>
    <p>Lorem ipsum dolor sit amet, consectetur adipisicing elit, sed do eiusmod tempor incididunt ut labore et dolore magna aliqua. Ut enim ad minim veniam, quis nostrud exercitation ullamco laboris nisi ut aliquip ex ea commodo consequat. Duis aute irure dolor in reprehenderit in voluptate velit esse cillum dolore eu fugiat nulla pariatur. Excepteur sint occaecat cupidatat non proident, sunt in culpa qui officia deserunt mollit anim id est laborum.</p>
    <h4>Certification</h4>
    <p>Personal Trainer Certification, Study Bundle, Fitness Nutrition Specialist, ABC Fitness Graduate</p>
    <h4>Get In Touch</h4>
    <div class="social">
      <span style="background:#3b5998"></span><span style="background:#1da1f2"></span><span style="background:#dd4b39"></span><span style="background:#c4302b"></span><span style="background:#e4405f"></span><span style="background:#1ab7ea"></span>
    </div>
    <a class="btn btn-solid about">About Company &nbsp;»</a>
  </div>
</section>

<section class="register">
  <h2>Register With Us</h2>
  <p>To get an unique fitness experience and nutrition chart to stay fit always.</p>
  <a class="btn btn-line signup">Signup Here &nbsp;»</a>
</section>

<section class="feedback">
  <div class="section-mark"></div>
  <h2 class="section-title">Feedback <span>We Recieved</span></h2>
  <p class="intro">Lorem ipsum dolor sit amet, consectetur adipisicing elit, sed do eiusmod tempor incididunt ut labore et dolore magna aliqua. Ut enim ad minim veniam, quis nostrud exercitation ullamco laboris nisi ut aliquip ex ea commodo consequat.</p>
  <div class="quotes">
    <div>
      <div class="quote">Etiam tristique sagittis pulvinar. Cras scelerisque dui ut, bibendum ante. dit neque eget lobortis. Nam eleifend sollicitudin nulla quis interdum et fames.</div>
      <div class="person"><div class="avatar" role="img" aria-label="Client photo"></div><div><b>Lena Ortiz</b><small>Issue, Istanbul</small></div></div>
    </div>
    <div>
      <div class="quote">Etiam tristique sagittis pulvinar. Cras scelerisque dui ut, bibendum ante. dit neque eget lobortis. Nam eleifend sollicitudin nulla quis interdum et fames.</div>
      <div class="person"><div class="avatar" role="img" aria-label="Client photo"></div><div><b>Marcus Hale</b><small>Issue, Istanbul</small></div></div>
    </div>
    <div>
      <div class="quote">Etiam tristique sagittis pulvinar. Cras scelerisque dui ut, bibendum ante. dit neque eget lobortis. Nam eleifend sollicitudin nulla quis interdum et fames.</div>
      <div class="person"><div class="avatar" role="img" aria-label="Client photo"></div><div><b>Priya Nolan</b><small>Issue, Istanbul</small></div></div>
    </div>
  </div>
</section>

<footer class="site-footer">
  <div class="brand"><span class="mark"></span><span class="name">Anchored Willow</span></div>
  <nav class="footer-nav">
    <span class="active">Home</span><span>Services</span><span>Success Story</span><span>About</span><span>Contacts</span><span>Sign In</span><span>Signup</span><span>Testimonials</span><span>Privacy Policy</span><span>Terms</span>
  </nav>
  <div class="footer-social"><span></span><span></span><span></span></div>
</footer>
<div class="copyright">© 2017 ANCHORED WILLOW<span class="up"></span></div>

</body>
</html>
```